Carpet cleaning company wants business card

Need an exciting new fresh design for business cards for my carpet cleaning /pest control business
www.tidewellhomecare.com.au
Can design include a lined section for quoting or information? Thanks !

```html
<!DOCTYPE html>
<html lang="en">
<head>
<meta charset="utf-8">
<title>Tidewell Home Care – Business Card</title>
<link href="https://fonts.googleapis.com/css2?family=Arimo:wght@400;700&display=swap" rel="stylesheet">
<style>
  :root {
    --stage: #2a2a2a;
    --card-front: #ffffff;
    --card-back: #333333;
    --brand-blue: #1f4fa8;
    --brand-red: #e33b3b;
    --text-light: #ffffff;
    --rule-light: #5a5a5a;
    --rule-dark: #d4d9e4;
  }
  * { box-sizing: border-box; margin: 0; padding: 0; }
  html, body {
    width: 1200px;
    height: 689px;
    overflow: hidden;
    background: var(--stage);
    font-family: "Arimo", Arial, sans-serif;
  }
  .stage {
    position: relative;
    width: 1200px;
    height: 689px;
  }
  .card {
    position: absolute;
    top: 200px;
    width: 480px;
    height: 290px;
    border-radius: 22px;
    overflow: hidden;
  }
  .card-front {
    left: 90px;
    background: var(--card-front);
  }
  .card-front .brand-name {
    position: absolute;
    left: 0;
    right: 0;
    top: 92px;
    text-align: center;
    font-size: 42px;
  }
  .card-back {
    left: 630px;
    background: var(--card-back);
    padding: 42px 40px;
  }
  .brand-name {
    font-weight: 700;
    color: var(--brand-blue);
    letter-spacing: -0.5px;
    line-height: 1;
    white-space: nowrap;
  }
  .card-back .brand-name { font-size: 30px; }
  .holder {
    margin-top: 26px;
  }
  .holder-name {
    font-weight: 700;
    font-size: 21px;
    color: var(--brand-blue);
  }
  .holder-role {
    font-size: 13px;
    color: var(--brand-red);
    margin-top: 2px;
  }
  .contact-list {
    list-style: none;
    margin-top: 22px;
  }
  .contact-item {
    display: flex;
    align-items: center;
    gap: 10px;
    font-size: 14px;
    color: var(--text-light);
    line-height: 1.45;
  }
  .contact-icon {
    width: 12px;
    height: 12px;
    flex: none;
    fill: var(--brand-blue);
    stroke: var(--brand-blue);
  }
  .note-lines {
    position: absolute;
    display: flex;
    flex-direction: column;
    justify-content: space-between;
  }
  .note-line {
    height: 0;
    border-top: 1px solid;
  }
  .card-front .note-lines {
    left: 50px;
    right: 50px;
    top: 178px;
    height: 72px;
  }
  .card-front .note-line { border-color: var(--rule-dark); }
  .card-back .note-lines {
    left: 300px;
    right: 40px;
    top: 118px;
    height: 124px;
  }
  .card-back .note-line { border-color: var(--rule-light); }
</style>
</head>
<body>
<main class="stage">

  <section class="card card-front" aria-label="Business card front">
    <p class="brand-name">Tidewell Home Care</p>
    <div class="note-lines" aria-label="Lined area for quotes">
      <span class="note-line"></span>
      <span class="note-line"></span>
      <span class="note-line"></span>
      <span class="note-line"></span>
    </div>
  </section>

  <section class="card card-back" aria-label="Business card back">
    <p class="brand-name">Tidewell Home Care</p>

    <div class="holder">
      <p class="holder-name">Mark Dalton</p>
      <p class="holder-role">President</p>
    </div>

    <ul class="contact-list">
      <li class="contact-item">
        <svg class="contact-icon" viewBox="0 0 12 12" aria-hidden="true"><path stroke="none" d="M2.5 0.8l2 2.3-1.1 1.4c0.7 1.5 1.9 2.7 3.4 3.4l1.4-1.1 2.3 2-1 1.9C5.2 10.5 1.5 6.8 0.8 2z"/></svg>
        07 5120 3344
      </li>
      <li class="contact-item">
        <svg class="contact-icon" viewBox="0 0 12 12" aria-hidden="true"><rect x="3" y="0.8" width="6" height="10.4" rx="1" fill="none" stroke-width="1.3"/><circle cx="6" cy="9.4" r="0.7" stroke="none"/></svg>
        0412 556 209
      </li>
      <li class="contact-item">
        <svg class="contact-icon" viewBox="0 0 12 12" aria-hidden="true"><rect x="0.8" y="2.5" width="10.4" height="7" rx="0.6" fill="none" stroke-width="1.2"/><path d="M1 3l5 3.6L11 3" fill="none" stroke-width="1.2"/></svg>
        admin@tidewellhomecare.com.au
      </li>
      <li class="contact-item">
        <svg class="contact-icon" viewBox="0 0 12 12" aria-hidden="true"><circle cx="6" cy="6" r="5" fill="none" stroke-width="1.2"/><path d="M1 6h10M6 1c-2.4 2.8-2.4 7.2 0 10M6 1c2.4 2.8 2.4 7.2 0 10" fill="none" stroke-width="1"/></svg>
        www.tidewellhomecare.com.au
      </li>
    </ul>

    <div class="note-lines" aria-label="Lined area for notes">
      <span class="note-line"></span>
      <span class="note-line"></span>
      <span class="note-line"></span>
      <span class="note-line"></span>
      <span class="note-line"></span>
    </div>
  </section>

</main>
</body>
</html>
```